Revamp Current Website From 2012 TO 2018

We need a ravamp to our current website. I prefer a professional corporate modern feel to it.

My Current Website is www.brightlanepromoworks.biz. Please redesign the homepage and the /certs page first....see attached document for specific instructions..

There is a lot of content at the bottom but maybe we can shorten that by using titles and a pop up of the details or something so it doesnt take too mcuh space...or maybe a red more hyperlink to see the rest of info in pop up or something or new page...

Target Market(s)

B2B, business owners, website owners, marketing companies.

Industry/Entity Type

Promotional Product

Number of Pages Required

2 page

Colors

Designer to choose colors to be used in the design.

Requirements
Must have
• Please keep in mind logo mock up I am working on that looks beautiful on dark background for header...see attached for logo
• Must use existing content I hope your marketing mind comes in to play when designing the website.
• Must have all my content provided on each page...
Nice to have
• similiar color scheme...
Should not have
• I dont like using templates because usually hard to expand on design in future so Prefer full custom designs
• Please no templates

```html
<!DOCTYPE html>
<html lang="en">
<head>
<meta charset="utf-8">
<title>Brightlane Promo Works – Home</title>
<link href="https://fonts.googleapis.com/css2?family=Source+Sans+3:wght@400;600;700;800&display=swap" rel="stylesheet">
<style>
:root{
  --brand-blue:#0a72c6;
  --ink-black:#101010;
  --page-dark:#231f20;
  --panel-light:#efefef;
  --text-dark:#3a3a3a;
  --white:#ffffff;
  --field:#e6e6e6;
}
*{box-sizing:border-box;margin:0;padding:0}
html,body{width:1200px;height:1200px;overflow:hidden}
body{background:var(--page-dark);font-family:"Source Sans 3",sans-serif;color:var(--white);position:relative}
.utility-bar{position:absolute;top:0;left:0;width:1200px;height:46px;background:var(--brand-blue)}
.contact-line{position:absolute;left:88px;top:16px;font-size:11px;display:flex;gap:6px;align-items:center}
.contact-line svg{width:7px;height:10px}
.login-form{position:absolute;left:702px;top:9px;display:flex;height:28px}
.login-form span{display:block;width:131px;background:var(--field);color:#9a9a9a;font-size:11px;text-align:center;line-height:28px}
.login-form span:first-child{border-radius:14px 0 0 14px;border-right:2px solid #ccc}
.login-form .login-btn{width:60px;background:var(--ink-black);color:#ddd;border-radius:0 14px 14px 0}
.signup-btn{position:absolute;left:1052px;top:9px;width:60px;height:28px;border-radius:14px;background:var(--ink-black);color:#ddd;font-size:11px;text-align:center;line-height:28px}
.main-nav{position:absolute;top:46px;left:0;width:1200px;height:46px;background:var(--ink-black)}
.brand{position:absolute;left:90px;top:16px;display:flex;align-items:center;gap:7px;font-weight:700;font-size:13px;letter-spacing:.5px;color:var(--brand-blue)}
.brand i{display:block;width:14px;height:14px;background:var(--brand-blue)}
.nav-links{position:absolute;top:10px;left:498px;display:flex;font-size:11px;color:#ddd}
.nav-links a{display:block;height:28px;line-height:28px;text-align:center;color:inherit;text-decoration:none}
.nav-links a.active{background:#1c2430;color:var(--brand-blue);border-radius:14px}
.hero{position:absolute;left:61px;top:118px;width:1079px;height:443px;overflow:hidden}
.hero-photo{position:absolute;inset:0;background:linear-gradient(120deg,#6b5a4a 0%,#4d3a45 35%,#6a4a6d 55%,#d8d4d2 80%,#8a7766 100%)}
.hero-title{position:absolute;left:28px;top:84px;font-size:47px;font-weight:800;line-height:54px;letter-spacing:-.5px}
.hero-facts{position:absolute;left:28px;top:218px;font-size:16.5px;line-height:20px}
.hero-cta{position:absolute;right:0;top:185px;width:329px;height:74px;background:var(--brand-blue);border-radius:37px 0 0 37px;display:flex;align-items:center;justify-content:center;gap:10px;font-weight:700;font-size:22px}
.incentives{position:absolute;left:61px;top:595px;width:1079px;height:257px;background:var(--brand-blue)}
.incentives h2{position:absolute;left:28px;top:26px;font-size:42px;font-weight:800}
.incentive-cols{position:absolute;left:28px;top:123px;display:flex}
.incentive-cols ul{list-style:none;width:262px;font-size:16.5px;line-height:20px;border-left:1px solid rgba(255,255,255,.7);padding-left:13px}
.incentive-cols ul:first-child{border-left:none;padding-left:0;width:250px}
.feature{position:absolute;left:61px;top:881px;width:1079px;height:256px;background:var(--panel-light)}
.feature-photo{position:absolute;left:0;top:0;width:526px;height:256px;background:linear-gradient(90deg,#c9c9c4,#ececea 50%,#bdbdb8)}
.feature h3{position:absolute;left:553px;top:29px;width:500px;color:var(--brand-blue);font-size:21px;font-weight:700;line-height:25px}
.feature p{position:absolute;left:553px;top:136px;width:500px;color:var(--text-dark);font-size:16px;line-height:20px}
.next-panel{position:absolute;left:61px;top:1169px;width:1079px;height:40px;background:var(--panel-light)}
</style>
</head>
<body>
<header class="utility-bar">
  <div class="contact-line">
    <svg viewBox="0 0 7 10"><rect x=".5" y=".5" width="6" height="9" rx="1" fill="none" stroke="#fff"/></svg>415-555-0138 (USA Office) &nbsp;|&nbsp;
    <svg viewBox="0 0 7 10"><rect x=".5" y=".5" width="6" height="9" rx="1" fill="none" stroke="#fff"/></svg>1-800-555-0147 (International)
  </div>
  <div class="login-form"><span>Username</span><span>Password</span><span class="login-btn">Login</span></div>
  <div class="signup-btn">Sing Up</div>
</header>
<nav class="main-nav">
  <div class="brand"><i></i>BRIGHTLANE PROMO WORKS</div>
  <div class="nav-links">
    <a class="active" style="width:88px">HOME</a>
    <a style="width:90px">OUR INCENTIVES</a>
    <a style="width:70px">SAMPLES</a>
    <a style="width:100px">HOW IT WORKS</a>
    <a style="width:80px">TESTIMONIALS</a>
    <a style="width:110px">FAQ</a>
    <a style="width:80px">CONTACT</a>
  </div>
</nav>
<section class="hero">
  <div class="hero-photo" role="img" aria-label="Tablet, pen and glasses on a wooden desk"></div>
  <h1 class="hero-title">BRIGHTLANE PROMO<br>WORKS</h1>
  <div class="hero-facts">12 Years In Business<br>13,000+ Clients Enrolled<br>2+ Million Certificates In Circulation<br>170,000 + Redemptions To Date<br>A Rating TRB<br>Licensed Seller Of Travel CST #5550192</div>
  <div class="hero-cta">RISK FREE FOR 30 DAYS
    <svg width="20" height="20" viewBox="0 0 20 20"><circle cx="10" cy="10" r="10" fill="#fff"/><path d="M8 5l5 5-5 5" stroke="#0a72c6" stroke-width="3" fill="none"/></svg>
  </div>
</section>
<section class="incentives">
  <h2>OUR INCENTIVES</h2>
  <div class="incentive-cols">
    <ul><li>• Airfare &amp; Hotel - U.S. ONLY</li><li>• 7 Night Resort</li><li>• 1-4 Night Las Vegas</li><li>• Luxurious Mexico Beach Resort</li><li>• Golf N' Stay In Cabo San Lucas</li></ul>
    <ul><li>• 1 Night Hotel Stay</li><li>• 2 Night Hotel Stay</li><li>• 3 Night Hotel Stay</li><li>• 4 Night Hotel Stay</li><li>• 7 inch Wi-Fi Tablet</li></ul>
    <ul><li>• Touch Mp4 Player</li><li>• Mini Digital Camcorder</li><li>• New Premium Quality Earbuds</li><li>• Premium $25 Restaurant Gift</li><li>• $300 Restaurant Certificate</li></ul>
    <ul><li>• Premium $50 CB Gros</li><li>• Premium $50 CB Gas</li><li>• Premium $100 Cash Back Gros</li><li>• Premium $100 Cash Back Gas</li><li>• Free Healthcare Discount Card</li></ul>
  </div>
</section>
<section class="feature">
  <div class="feature-photo" role="img" aria-label="Desktop monitor showing a climb to success growth chart"></div>
  <h3>INCREASE LEADS AND SALES FROM YOUR EXISTING MARKETING EFFORTS BY OFFERING HIGH PERCEIVED VALUE INCENTIVES TO YOUR CUSTOMERS!</h3>
  <p>Create a variety giveaway promotions for your business with an unlimited supply of top quality vacation getaway certificates, restaurant gift certificates, electronic product giveaways and gas or grocery rewards for just $99/mth. Whether you need 100 or 100,000 you will never pay more than $99.</p>
</section>
<div class="next-panel"></div>
</body>
</html>
```